Business card design

I already have the logo design completed and am requiring business card design and layout utilising the logo. I require a front and back design.

We are an executive recruitment company so we are looking at full colour, high finish in a reasonably conservative structure.
Updates

Reason: will be provide ai template

Target Market(s)

Senior Management 35-60 age bracket

Industry/Entity Type

Business

Requirements
Must have
• Tobias Wrenfield
• Director
• 48 Morrow Pde, Paddington QLD 4071
• Ph: 07 3944 2618 Mob: 0468925317
• tobias@orvandaexecutive.com.au
• www.orvandaexecutive.com.au
Nice to have
• Ideally full colour,
Should not have
• cheap looking

```html
<!DOCTYPE html>
<html lang="en">
<head>
<meta charset="utf-8">
<title>Orvanda Executive – Business Card</title>
<link rel="stylesheet" href="https://fonts.googleapis.com/css2?family=Source+Sans+3:wght@400;600;700&display=swap">
<style>
  :root {
    --backdrop: #686868;
    --card-white: #ffffff;
    --navy: #143a6b;
    --grey-text: #6b6b6b;
    --light-grey-text: #a3a3a3;
    --stripe-top: #0b4a82;
    --stripe-bottom: #0f2c58;
    --back-top: #0c4677;
    --back-bottom: #152a55;
    --edge-light: #9a9a9a;
    --edge-dark: #111111;
    --white: #ffffff;
  }
  * { margin: 0; padding: 0; box-sizing: border-box; }
  html, body {
    width: 1200px;
    height: 900px;
    overflow: hidden;
    background: var(--backdrop);
    font-family: "Source Sans 3", sans-serif;
  }
  .card {
    position: absolute;
    left: 304px;
    width: 593px;
    height: 329px;
    overflow: hidden;
  }
  .card--front { top: 80px; background: var(--card-white); }
  .card--back {
    top: 491px;
    background: linear-gradient(180deg, var(--back-top) 0%, var(--back-bottom) 100%);
  }
  .edge-stripe {
    position: absolute;
    top: 0; right: 0;
    width: 12px; height: 100%;
  }
  .card--front .edge-stripe {
    background: linear-gradient(180deg, var(--stripe-top), var(--stripe-bottom));
  }
  .card--back .edge-stripe {
    background: linear-gradient(180deg, var(--edge-light) 0%, var(--edge-light) 45%, var(--edge-dark) 100%);
  }

  .wordmark {
    position: absolute;
    display: flex;
    align-items: center;
    gap: 20px;
    font-weight: 600;
  }
  .wordmark__dot {
    width: 58px; height: 58px;
    border-radius: 50%;
    flex: none;
  }
  .wordmark__text { line-height: 1; }
  .wordmark__name { display: block; font-size: 36px; letter-spacing: 1px; }
  .wordmark__tag { display: block; font-size: 11px; letter-spacing: 10px; margin-top: 5px; }

  .card--front .wordmark { left: 49px; top: 47px; color: var(--navy); }
  .card--front .wordmark__dot { background: var(--navy); }
  .card--back .wordmark { left: 50%; top: 136px; transform: translateX(-50%); color: var(--white); }
  .card--back .wordmark__dot { background: var(--white); }

  .holder {
    position: absolute;
    left: 47px; top: 175px;
  }
  .holder__name {
    font-size: 25px; font-weight: 700; color: var(--navy); line-height: 1.1;
  }
  .holder__role {
    font-size: 19px; font-weight: 400; color: var(--grey-text);
    letter-spacing: 1px; line-height: 1.2;
  }

  .contact {
    position: absolute;
    left: 318px; top: 173px;
    list-style: none;
    font-size: 16.5px;
    line-height: 25px;
    color: var(--light-grey-text);
  }
  .contact__num { letter-spacing: 1.5px; }

  .web-address {
    position: absolute;
    left: 0; right: 12px; top: 293px;
    text-align: center;
    font-size: 21px;
    letter-spacing: 0.8px;
    color: var(--white);
  }
</style>
</head>
<body>
  <section class="card card--front" aria-label="Card front">
    <div class="wordmark">
      <span class="wordmark__dot"></span>
      <span class="wordmark__text">
        <span class="wordmark__name">ORVANDA</span>
        <span class="wordmark__tag">EXECUTIVE</span>
      </span>
    </div>

    <div class="holder">
      <p class="holder__name">Tobias Wrenfield</p>
      <p class="holder__role">Director</p>
    </div>

    <ul class="contact">
      <li>48 Morrow Pde, Ashcombe</li>
      <li>QLD 4071</li>
      <li class="contact__num">P: 07 3944 2618</li>
      <li class="contact__num">M: 0468 925 317</li>
      <li>tobias@orvandaexecutive.com.au</li>
    </ul>

    <div class="edge-stripe"></div>
  </section>

  <section class="card card--back" aria-label="Card back">
    <div class="wordmark">
      <span class="wordmark__dot"></span>
      <span class="wordmark__text">
        <span class="wordmark__name">ORVANDA</span>
        <span class="wordmark__tag">EXECUTIVE</span>
      </span>
    </div>

    <p class="web-address">www.orvandaexecutive.com.au</p>

    <div class="edge-stripe"></div>
  </section>
</body>
</html>
```